Toval Botanics Website Revamping for Ecommerce

Looking to upgrade our website and provide a better experience to users both visually and from a navigation standpoint. Here is our current site

http://tovalbotanics dot example/

Below are some Shopify Design Concepts We Like.
https://lindworp. example/pages/classic
https://www.gorvamunch. example/
https://www.merrowquintile. example/

Target Market(s)

People with Darker Skin Tone (Black and Brown)

Industry/Entity Type

Skin Care Product

Number of Pages Required

4 page

Requirements
Must have
• Use the Brand Guide
Nice to have
• Focus on E-Commerce Platforms such as Shopify but can be other platforms too
Should not have
• Don't deviate from Brand Guide (Attached)

```html
<!DOCTYPE html>
<html lang="en">
<head>
<meta charset="utf-8">
<title>Toval Botanics — Rule Your Skin</title>
<link href="https://fonts.googleapis.com/css2?family=Montserrat:wght@400;600;700&family=Questrial&display=swap" rel="stylesheet">
<style>
:root{
  --green:#1a9a4a;
  --green-dark:#0f7a37;
  --green-soft:#e3f4ea;
  --mint:#e8f6ef;
  --peach:#f7e6d6;
  --ink:#2b2b2b;
  --muted:#6d6d6d;
  --white:#ffffff;
  --brown:#5a3a2a;
  --photo-warm:#6b5040;
  --photo-grey:#4a4a4a;
}
*{box-sizing:border-box;margin:0;padding:0}
html,body{width:1200px;height:4157px;overflow:hidden}
body{position:relative;background:var(--white);font-family:"Questrial",sans-serif;color:var(--ink)}
.abs{position:absolute}
.heading{position:absolute;left:0;width:1200px;text-align:center;font-family:"Montserrat",sans-serif;font-weight:600;font-size:25px;color:var(--ink)}
.heading::after{content:"";display:block;width:40px;height:2px;background:var(--green);margin:10px auto 0}
.heading::before{content:"";display:block;width:12px;height:12px;border-radius:50%;background:var(--green);margin:0 auto 8px}

/* hero */
.hero{left:0;top:0;width:1200px;height:620px}
.hero-photo{position:absolute;inset:0;background:linear-gradient(90deg,var(--photo-grey) 0%,#5d5752 45%,var(--photo-warm) 70%,#8a7a3a 100%)}
.hero-shade{position:absolute;inset:0;background:linear-gradient(90deg,rgba(40,40,40,.55),rgba(40,40,40,0) 60%)}
.logo{left:128px;top:60px;font-family:"Questrial",sans-serif;font-size:52px;color:var(--white);letter-spacing:2px}
.nav{left:445px;top:88px;display:flex;gap:32px;font-size:14px;color:var(--white)}
.social{left:770px;top:86px;display:flex;gap:8px}
.social span{width:14px;height:14px;border-radius:50%;background:rgba(255,255,255,.8)}
.cart{left:925px;top:78px;width:142px;height:36px;border-radius:18px;background:var(--white);display:flex;align-items:center;padding-left:14px;font-size:13px;color:var(--ink)}
.cart i{position:absolute;right:3px;top:3px;width:44px;height:30px;border-radius:15px;background:var(--green)}
.hero-title{left:155px;top:228px;color:var(--white);font-family:"Montserrat",sans-serif}
.hero-title h1{font-size:36px;font-weight:700;letter-spacing:1px}
.hero-title p{font-size:36px;font-weight:400;margin-top:2px}
.hero-list{left:158px;top:325px;list-style:none;color:var(--white);font-size:16px;line-height:26px}
.hero-list li::before{content:"✓";margin-right:14px}
.btn{display:inline-flex;align-items:center;justify-content:center;background:var(--green);color:var(--white);border-radius:18px;font-size:13px}
.shop{left:155px;top:428px;width:130px;height:34px}
.arrow{top:295px;width:34px;height:40px;border:2px solid rgba(255,255,255,.7);border-radius:3px}

/* washes */
.wash-green{left:0;top:1240px;width:1200px;height:1080px;background:radial-gradient(ellipse at 50% 40%,#d2efe0 0%,#e6f6ee 55%,rgba(255,255,255,0) 80%)}
.wash-peach{left:0;top:2700px;width:1200px;height:640px;background:radial-gradient(ellipse at 50% 55%,#f4dcc6 0%,#f8ebde 55%,rgba(255,255,255,0) 80%)}
.leaf{background:#8fc46a;border-radius:60% 10% 60% 10%;opacity:.85}

/* products */
.product{top:833px;width:202px;height:385px;background:var(--white);text-align:center;box-shadow:0 1px 6px rgba(0,0,0,.06)}
.product.active{box-shadow:0 4px 22px rgba(0,0,0,.18)}
.product .bottle{margin:40px auto 0;width:70px;height:200px;border-radius:12px 12px 6px 6px;background:linear-gradient(90deg,#0c6a2e,#27a557,#0c6a2e)}
.product h3{font-weight:400;font-size:15px;margin-top:34px}
.stars{color:var(--green);font-size:12px;letter-spacing:2px;margin-top:10px}
.price{font-family:"Montserrat",sans-serif;font-weight:600;font-size:15px;margin-top:8px}
.price s{color:var(--muted);font-weight:400;margin-right:8px}
.mini-cart{width:14px;height:14px;border-radius:50%;background:var(--green-soft);margin:20px auto 0}
.cart-round{left:457px;top:1195px;width:50px;height:50px;border-radius:50%;background:var(--green)}
.sale{right:0;top:0;width:0;height:0;border-top:46px solid var(--brown);border-left:46px solid transparent}

/* ingredients */
.ingredient{top:1430px;width:146px;text-align:center}
.ingredient .ring{width:146px;height:146px;border-radius:50%;border:4px solid var(--white);box-shadow:0 2px 8px rgba(0,0,0,.12)}
.ingredient.active .ring{border-color:var(--green)}
.ingredient p{font-size:15px;margin-top:22px}
.ingredient-copy{left:300px;top:1675px;width:600px;text-align:center;font-size:14px;line-height:19px;color:#444}

/* stories */
.story{top:1900px;width:280px;height:276px;overflow:hidden}
.story .img{width:100%;height:100%}
.story .caption{position:absolute;left:0;bottom:0;width:100%;height:56px;background:var(--green);color:var(--white);font-size:13px;line-height:17px;padding:10px 14px}
.story.featured .img{background:var(--green)}
.story.featured .text{position:absolute;left:14px;top:100px;right:14px;color:var(--white);font-size:14px;line-height:18px}

/* press */
.press{top:2500px;width:300px;text-align:center}
.press .name{font-size:36px;color:#111;height:50px}
.press p{font-size:13px;color:#555;margin-top:22px;line-height:17px}

/* blog */
.post{top:2795px;width:280px;height:385px;background:var(--white);box-shadow:0 2px 10px rgba(0,0,0,.08);text-align:center}
.post .img{height:165px}
.post .date{font-size:11px;color:var(--green);letter-spacing:1px;margin-top:20px}
.post h3{font-weight:400;font-size:16px;margin-top:10px}
.post p{font-size:13px;color:#555;line-height:17px;margin:18px 26px 0}
.post .more{font-size:13px;margin-top:26px}
.post .more::before{content:"";display:inline-block;width:11px;height:11px;border-radius:50%;background:var(--ink);margin-right:8px;vertical-align:-1px}

/* instagram */
.ig-nav{left:995px;top:3420px;font-size:18px;color:var(--muted)}
.ig-tile{top:3482px;width:172px;height:172px}

/* footer */
.footer{left:0;top:3654px;width:1200px;height:503px;background:linear-gradient(#e4f5ec,#f1faf5)}
.col h4{font-weight:400;font-size:16px;margin-bottom:22px}
.col p{font-size:13px;line-height:17px;color:#333}
.col b{font-weight:400;display:block;margin-top:14px;font-family:"Montserrat",sans-serif;font-weight:600;font-size:13px}
.field{width:300px;height:30px;border-radius:15px;background:var(--white);font-size:11px;color:#999;padding:8px 16px}
.send{width:100px;height:30px;margin-top:12px}
.circles{display:flex;gap:8px;margin-top:22px}
.circles span{width:24px;height:24px;border-radius:50%;border:1px solid var(--ink)}
.read-btn{width:92px;height:28px;background:var(--brown);color:var(--white);border-radius:14px;font-size:12px;margin-top:24px}
.watermark{left:78px;top:3965px;font-size:120px;color:rgba(0,0,0,.06)}
.top-btn{left:1052px;top:3960px;width:46px;height:46px;border-radius:50%;background:var(--brown)}
.top-label{left:1058px;top:4010px;font-size:11px}
.copy{left:0;top:4103px;width:1200px;text-align:center;font-size:12px;color:var(--muted)}
</style>
</head>
<body>

<!-- hero -->
<section class="abs hero">
  <div class="hero-photo" role="img" aria-label="Smiling woman with curly hair in soft natural light"></div>
  <div class="hero-shade"></div>
  <svg class="abs" style="left:0;bottom:0" width="1200" height="70" viewBox="0 0 1200 70"><path d="M0 70V30L60 40 120 22 180 48 260 30 340 52 420 36 520 55 600 40 680 58 760 34 840 50 920 30 1000 44 1080 18 1140 26 1200 10V70Z" fill="#fff"/></svg>
</section>
<div class="abs logo">toval</div>
<nav class="abs nav"><span>About Us</span><span>Go Natural</span><span>Contact Us</span></nav>
<div class="abs social"><span></span><span></span><span></span><span></span><span></span></div>
<div class="abs cart">My Cart Item<i></i></div>
<div class="abs hero-title"><h1>RULE YOUR SKIN</h1><p>In 3 Easy Steps</p></div>
<ul class="abs hero-list"><li>Refresh and clean</li><li>Moisturize and replenish</li><li>Hydrate and soothe</li></ul>
<div class="abs btn shop">Shop Now</div>
<div class="abs arrow" style="left:76px"></div>
<div class="abs arrow" style="left:1090px"></div>

<!-- background washes and leaves -->
<div class="abs wash-green"></div>
<div class="abs wash-peach"></div>
<div class="abs leaf" role="img" aria-label="Green leaf sprig" style="left:-10px;top:560px;width:90px;height:300px"></div>
<div class="abs leaf" role="img" aria-label="Green leaf sprig" style="left:1100px;top:1190px;width:100px;height:250px"></div>
<div class="abs leaf" role="img" aria-label="Green leaf sprig" style="left:-10px;top:2120px;width:110px;height:280px"></div>
<div class="abs leaf" role="img" aria-label="Green leaf sprig" style="left:1120px;top:2800px;width:80px;height:230px"></div>

<!-- featured products -->
<h2 class="heading" style="top:730px">Featured Products</h2>
<div class="abs product" style="left:158px"><div class="bottle" role="img" aria-label="Green tonic bottle"></div><h3>Purifying Tonic Lotion</h3><div class="stars">★★★★★</div><div class="price">$12.99</div><div class="mini-cart"></div></div>
<div class="abs product active" style="left:383px"><div class="bottle" role="img" aria-label="Green spray bottle"></div><h3>Facial Cream</h3><div class="stars">★★★★★</div><div class="price">$19.99</div></div>
<div class="abs cart-round"></div>
<div class="abs product" style="left:608px"><div class="bottle" role="img" aria-label="Green lotion bottle" style="width:90px"></div><h3>Body Lotion</h3><div class="stars">★★★★★</div><div class="price">$15.99</div><div class="mini-cart"></div></div>
<div class="abs product" style="left:833px"><div class="sale abs"></div><div class="bottle" role="img" aria-label="Three bottle bundle" style="width:150px;height:170px;margin-top:70px"></div><h3>Toval Bundle</h3><div class="stars">★★★★★</div><div class="price"><s>$48.97</s>$45.00</div><div class="mini-cart"></div></div>

<!-- ingredients -->
<h2 class="heading" style="top:1330px">Amazing Ingredients</h2>
<div class="abs ingredient" style="left:162px"><div class="ring" role="img" aria-label="Lavender bundle" style="background:#8b6bb8"></div><p>Lavender</p></div>
<div class="abs ingredient active" style="left:323px"><div class="ring" role="img" aria-label="Green tea leaves" style="background:#4f9a2c"></div><p>Green Tea</p></div>
<div class="abs ingredient" style="left:528px"><div class="ring" role="img" aria-label="Sliced cucumber" style="background:#3f7a2c"></div><p>Cucumber</p></div>
<div class="abs ingredient" style="left:717px"><div class="ring" role="img" aria-label="Jojoba fruit" style="background:#6c7a3a"></div><p>Jojoba-oil</p></div>
<div class="abs ingredient" style="left:897px"><div class="ring" role="img" aria-label="Bowl of citrus fruit" style="background:#e89a2c"></div><p>Citrus</p></div>
<p class="abs ingredient-copy">Green tea improves your skin complexion and makes your skin healthy. It helps flush out toxins from the skin, heals blemishes and scars, and reduces inflammation. It also improves the skin's elasticity.</p>

<!-- rule your skin -->
<h2 class="heading" style="top:1798px">Rule Your Skin</h2>
<div class="abs story" style="left:157px"><div class="img" role="img" aria-label="Woman smiling at her phone" style="background:linear-gradient(135deg,#7a4e9a,#3a2a2a)"></div><div class="caption">Toval found its source in the contention between our constant desire for...</div></div>
<div class="abs story featured" style="left:462px"><div class="img"></div><p class="text">When we found ourselves cornered we had two options either surrender to the rules of the market or turn the table and take control. We chose the latter.</p></div>
<div class="abs story" style="left:766px"><div class="img" role="img" aria-label="Laughing woman wearing a flower crown" style="background:linear-gradient(135deg,#3a3a3a,#c24a7a)"></div><div class="caption">Toval offers you three basic morning routines that can be summed up as follows...</div></div>

<!-- press -->
<h2 class="heading" style="top:2398px">People Are Talking</h2>
<div class="abs press" style="left:145px"><div class="name">Drifthour</div><p>"Toval says be proud of your skin and<br>embrace your color"</p></div>
<div class="abs press" style="left:450px"><div class="name" style="font-size:24px;padding-top:10px">Lumerra</div><p>"Heals and improves the skin's overall<br>appearance"</p></div>
<div class="abs press" style="left:755px"><div class="name">Quillpost</div><p>"Could totally change the skincare<br>industry for people of color"</p></div>

<!-- blog -->
<h2 class="heading" style="top:2698px">Our Latest Blog</h2>
<article class="abs post" style="left:157px"><div class="img" role="img" aria-label="Portrait of a smiling woman" style="background:linear-gradient(#3a2a22,#6a4a3a)"></div><div class="date">SEPTEMBER 15, 2016</div><h3>Purifying Tonic Lotion</h3><p>When rap artists Marlo and Keston unexpectedly released a collaboration album titled "What a time...</p><div class="more">Read More</div></article>
<article class="abs post" style="left:462px"><div class="img" role="img" aria-label="Woman talking on the phone" style="background:linear-gradient(#e8e8e8,#5a3a2a)"></div><div class="date">SEPTEMBER 29, 2016</div><h3>Funded with Fundmoor</h3><p>An hour before I sat down in front of my laptop to write these very words, our Fundmoor campaign...</p><div class="more" style="color:var(--green)">Read More</div></article>
<article class="abs post" style="left:766px"><div class="img" role="img" aria-label="Woman in a business jacket" style="background:linear-gradient(#dcdcdc,#3a2a22)"></div><div class="date">SEPTEMBER 15, 2016</div><h3>Purifying Tonic Lotion</h3><p>When rap artists Marlo and Keston unexpectedly released a collaboration album titled "What a time to...</p><div class="more">Read More</div></article>

<!-- instagram -->
<h2 class="heading" style="top:3377px">Instagram</h2>
<div class="abs ig-nav">←&nbsp;|&nbsp;→</div>
<div class="abs ig-tile" role="img" aria-label="Magazine cover" style="left:0;background:#b08a70"></div>
<div class="abs ig-tile" role="img" aria-label="Green product close-up" style="left:171px;background:#2a9a4a"></div>
<div class="abs ig-tile" role="img" aria-label="Green texture" style="left:342px;background:#3aa04a"></div>
<div class="abs ig-tile" role="img" aria-label="Woman at an event" style="left:514px;background:#c8c4be"></div>
<div class="abs ig-tile" role="img" aria-label="City skyline by the water" style="left:685px;background:linear-gradient(#6fb4e6,#3a8a9a)"></div>
<div class="abs ig-tile" role="img" aria-label="Aerial city view" style="left:857px;background:linear-gradient(#8ab4d4,#4a6a5a)"></div>
<div class="abs ig-tile" role="img" aria-label="Tea plantation terraces" style="left:1028px;background:#4a9a2a"></div>

<!-- footer -->
<footer class="abs footer"></footer>
<div class="abs watermark">toval</div>
<div class="abs col" style="left:157px;top:3756px;width:210px"><h4>About The Journey</h4><p>It is a long established fact that a reader will be distracted by the readable content of a page when looking at its layout. The point of using Lorem Ipsum is that it has a more-or-less normal distribution like readable English publishing packages and web page editors.</p><div class="abs btn read-btn" style="position:static">Read More</div></div>
<div class="abs col" style="left:460px;top:3756px"><h4>Newsletter</h4><div class="field">Enter Your Email...</div><div class="btn send">Send</div><div class="circles"><span></span><span></span><span></span><span></span><span></span></div></div>
<div class="abs col" style="left:815px;top:3756px;width:220px"><h4>Contact Us</h4><b style="margin-top:0">Address:</b><p>118 Harrow Lane, 3rd Floor Bayview, FL 30000</p><b>Phone:</b><p>(800) 555-0142</p><b>Email:</b><p>info@tovalbotanics.example</p></div>
<div class="abs top-btn"></div>
<div class="abs top-label">TOP</div>
<div class="abs copy">© 2017, Toval Cosmetics. All Rights Reserved.</div>

</body>
</html>
```